Southeast TLP Experience = More Sales

I am looking for a Professional Brochure that is geared towards the C-Suite member. Please feel free to change pictures, colors, number of columns per page, etc. If you have a way to change the charts to better fit your design feel free to do so. If you need additional information or revised picture, logo - please let me know.

Our website is www.brovantek.com or www.quillmarabenefit.com

Target Market(s)

Large Employers in the Southeast US

Industry/Entity Type

Insurance Broker

Font styles to use
Serif

Requirements
Must have
• High quality professionalism with an audience of CEO, CFO and Human Resource Professionals. I have left the cover blank so that you can create that. I do want to have the last page on the outside back cover.
Nice to have
• Creative design, to include graphics, Charts,
Should not have
• If these photos that I have included are not of the best quality to show your work, feel free to utilize others.

```html
<!DOCTYPE html>
<html lang="en">
<head>
<meta charset="utf-8">
<title>TLP Experience – Brochure Spread</title>
<link rel="stylesheet" href="https://fonts.googleapis.com/css2?family=PT+Sans:ital,wght@0,400;0,700;1,400;1,700&display=swap">
<style>
  :root{
    --bg:#dcdcd8;
    --paper:#f7f7f5;
    --ink:#2f2f2f;
    --muted:#9a9a9a;
    --navy:#243a7a;
    --red:#9b2d2a;
    --orange:#d89a2a;
    --teal:#5a9e88;
    --olive:#9cb548;
    --purple:#4a3a66;
    --quote:#4f7fb8;
  }
  *{box-sizing:border-box;margin:0;padding:0}
  html,body{width:1200px;height:804px;overflow:hidden;background:var(--bg)}
  body{font-family:"PT Sans",sans-serif;color:var(--ink);position:relative}
  .spread{position:absolute;left:40px;top:30px;width:1120px;height:744px;display:flex;box-shadow:0 8px 24px rgba(0,0,0,.18)}
  .page{position:relative;width:560px;height:744px;background:var(--paper);overflow:hidden}
  .page--left{background:linear-gradient(90deg,var(--paper) 88%,#e6e6e3 100%)}
  .page--right{background:linear-gradient(90deg,#e4e4e1 0%,var(--paper) 10%)}
  .running-head{position:absolute;top:24px;right:70px;font-size:9px;color:var(--muted)}
  .corner-tab{position:absolute;top:0;right:24px;width:36px;height:26px;background:var(--navy);clip-path:polygon(0 0,100% 0,100% 100%,40% 100%)}
  .page-foot{position:absolute;bottom:0;left:0;display:flex;align-items:center;gap:14px}
  .page-num{width:52px;height:34px;background:var(--navy);color:#fff;font-size:12px;font-weight:700;display:flex;align-items:center;padding-left:14px;clip-path:polygon(0 0,60% 0,100% 100%,0 100%)}
  .page-url{font-size:9px;color:var(--muted)}
  .title{position:absolute;left:48px;top:92px;font-size:34px;font-weight:400;letter-spacing:.5px;color:#444}
  .title strong{font-weight:700;color:#333}
  .process{position:absolute;left:40px;top:185px}
  .columns{position:absolute;display:grid;grid-template-columns:1fr 1fr;column-gap:26px}
  .page--left .columns{left:48px;top:380px;width:470px}
  .page--right .columns{left:54px;top:74px;width:470px}
  h2{font-size:13px;font-weight:700;margin:0 0 6px;color:#333}
  .section-title{font-size:13px;margin-bottom:8px}
  p{font-size:9.2px;line-height:1.32;text-align:justify;margin-bottom:12px;color:#3a3a3a}
  .block{margin-bottom:6px}
  .photo{position:absolute;left:54px;top:362px;width:470px;height:240px;border-radius:18px;
    background:radial-gradient(ellipse at 55% 50%,#b59a5c 0%,#8f7a4e 22%,#c9c1a6 45%,#a59f88 75%,#7d7866 100%)}
  .quote{position:absolute;left:62px;top:622px;width:460px;height:60px}
  .quote-mark{position:absolute;font-size:64px;font-weight:700;color:#8a8a8a;line-height:1}
  .quote-mark--open{left:0;top:6px}
  .quote-mark--close{right:0;top:-16px}
  .quote-text{position:absolute;left:44px;top:10px;font-size:11px;font-style:italic;font-weight:700;color:var(--quote)}
  .quote-note{position:absolute;right:44px;top:28px;font-size:9px;color:#555}
</style>
</head>
<body>
<div class="spread">
  <section class="page page--left">
    <span class="running-head">Halden Partners</span>
    <span class="corner-tab"></span>
    <h1 class="title"><strong>TLP</strong> EXPERIENCE...</h1>

    <svg class="process" width="480" height="170" viewBox="0 0 480 170" aria-label="Five step process">
      <g fill="none" stroke-width="1.6">
        <path d="M52 132 Q80 150 102 128" stroke="var(--red)"/>
        <path d="M150 40 Q185 0 215 30" stroke="var(--orange)"/>
        <path d="M245 130 Q270 150 300 120" stroke="var(--teal)"/>
        <path d="M335 42 Q360 8 385 34" stroke="var(--olive)"/>
      </g>
      <g font-family="PT Sans, sans-serif" font-size="9" fill="#444">
        <rect x="16" y="70" width="82" height="64" rx="4" fill="#fff" stroke="#d8a9a4"/>
        <text x="30" y="95">Starter Kit</text>
        <rect x="118" y="52" width="82" height="64" rx="4" fill="#fff" stroke="#e8cc9a"/>
        <text x="126" y="90">Starter Session</text>
        <rect x="216" y="64" width="82" height="64" rx="4" fill="#fff" stroke="#a9cfc2"/>
        <text x="234" y="88">BluePrint</text>
        <rect x="312" y="52" width="84" height="64" rx="4" fill="#fff" stroke="#cddba4"/>
        <text x="322" y="84">Implementation</text>
        <text x="322" y="96">/ Engage</text>
        <rect x="412" y="56" width="66" height="60" rx="4" fill="#fff" stroke="#b9b3c6"/>
        <text x="418" y="80">Accountability</text>
      </g>
      <g font-family="PT Sans, sans-serif" font-size="14" font-weight="700" fill="#fff">
        <rect x="34" y="118" width="64" height="24" fill="var(--red)"/><text x="56" y="135">01</text>
        <rect x="128" y="38" width="60" height="22" fill="var(--orange)"/><text x="149" y="54">02</text>
        <rect x="230" y="114" width="62" height="22" fill="var(--teal)"/><text x="252" y="130">03</text>
        <rect x="320" y="36" width="62" height="22" fill="var(--olive)"/><text x="342" y="52">04</text>
        <rect x="418" y="110" width="60" height="22" fill="var(--purple)"/><text x="439" y="126">05</text>
      </g>
    </svg>

    <div class="columns">
      <div>
        <div class="block"><h2>Starter Kit</h2>
          <p>The process begins with an honest evaluation from the leaders of your company using the "starter kit". We will ask that each leader complete this process independently, which allows Halden Partners to quickly understand where there is alignment and more importantly misalignment of a prospective clients employee benefit goals and objectives.</p></div>
        <div class="block"><h2>Starter Session</h2>
          <p>To gain clarification and deeper insight to a prospective clients situation, we will engage in this interactive session to see if there might be any obstacles or an opportunity to maximize your strategy.</p></div>
        <div class="block"><h2>BluePrint</h2>
          <p>This a customized step by step multi year plan that is aligned with your professionals and ours to execute and achieve your vision. Overall success in creating this competitive advantage will drive an employers overall business success.</p></div>
      </div>
      <div>
        <div class="block"><h2>Implementation/Engage</h2>
          <p>First, prospective clients will be in an informed position to make an objective decision on how we provide value and drive results. Second and of equal importance, our team will understand whether a prospective client is a "good fit" for our organization. Halden Partners wants to work exclusively with employers who consider their strategic initiative to achieving their overall corporate goals—not just a budget line item.</p></div>
        <div class="block"><h2>Accountability</h2>
          <p>Halden Partners looks forward to our working with relationship with each prospective client. Once we have been retained we embrace the idea of being held accountable for results. Based on the final decisions laid out in the BluePrint everyone will know the expectations and how those will be measured throughout the year as well as given a Service Calendar for the entire year.</p></div>
      </div>
    </div>

    <div class="page-foot"><span class="page-num">16</span><span class="page-url">www.brovantek.com</span></div>
  </section>

  <section class="page page--right">
    <span class="running-head">Halden Partners</span>
    <span class="corner-tab"></span>
    <div class="columns">
      <div>
        <h2 class="section-title">Benefit Strategies..</h2>
        <p>We specialize in empowering employers with the knowledge and tools to offer exceptional benefit programs for their employees. Obtaining access to quality and affordable health care is what matters most each and every day. It goes beyond than just simply providing a health care product. Halden Partners work to identify as well as understand our clients' organizational challenges, then we collaborate to put strategies in place to deliver their desired outcomes.</p>
        <p>By utilizing the latest actuarially developed tools, Halden Partners is able to provide employers with the precise information needed to manage plan cost and utilization. We focus on improving the performance of the benefit programs by creating a benefits strategy to maximize the value on the benefit dollars spent.</p>
        <p>These days there is a lot of risk associated with an employer-sponsored health care plan. As employers deal with rising health care cost and the added regulations put in place by the government, many are struggling to</p>
      </div>
      <div>
        <p>manage these risk. Just like you can't build a solid structure without a blueprint, you can't create an effective benefit package without a strategy.</p>
        <p>As the largest true independent agency in the Carolinas, we partner with like-minded employers who have a genuine interest in improving their benefit offering as well as the long term financial well-being of the benefit package. This partnership, should be grounded in disciplined, structured analysis and address not only the issues of today, but also consider the obstacles on the horizon. We have found this ties together a fragmented health care system and empowers both the employee and employer on to be maximum their healthcare savings.</p>
        <p>We feel there are numerous ways for an employer to create and fund an attractive healthcare plan. By combining our collective power and coordinating resources we can build a long term plan through a sea of insurance carriers and funding structures.</p>
      </div>
    </div>

    <div class="photo" role="img" aria-label="Photo of a brass compass resting on an old map"></div>

    <div class="quote">
      <span class="quote-mark quote-mark--open">“</span>
      <span class="quote-text">When it comes to Employee Benefits, the path is not the same for Everyone.</span>
      <span class="quote-note">Each Client has unique needs.</span>
      <span class="quote-mark quote-mark--close">”</span>
    </div>

    <div class="page-foot"><span class="page-num">17</span><span class="page-url">www.brovantek.com</span></div>
  </section>
</div>
</body>
</html>
```